Business Card Design Project

We need a business card design for a consultancy called 'Maple Ridge'. The design should communicate innovation and professionalism. The colors used should complement our logo. Please include source files for winning design.
Updates

Industry/Entity Type

Business

Colors

Designer to choose colors to be used in the design.

Requirements
Must have
• Card size should be 85mm x 50mm. The back side of the card should be the logo on a black background. The front side should display the name 'Maple Ridge' along with standard information. The front's design should graphically complement the back.
Nice to have
• Any graphical elements in the front the complement the back side (with the logo on a black background) would be a plus.

```html
<!DOCTYPE html>
<html lang="en">
<head>
<meta charset="utf-8">
<title>Maple Ridge — Business Card</title>
<link rel="stylesheet" href="https://fonts.googleapis.com/css2?family=Cinzel:wght@600&family=Questrial&display=swap">
<style>
  :root {
    --backdrop: #3a3a3c;
    --card-white: #f3f4f6;
    --card-black: #141414;
    --accent: #f0871e;
    --accent-soft: #e9a960;
    --ink: #1e1e1e;
    --grunge: #d9dadc;
  }
  * { box-sizing: border-box; margin: 0; padding: 0; }
  html, body { width: 1200px; height: 831px; overflow: hidden; }
  body {
    background: var(--backdrop);
    font-family: "Questrial", "Century Gothic", sans-serif;
    position: relative;
  }
  .card {
    position: absolute;
    width: 540px;
    height: 318px;
    border-radius: 3px;
    box-shadow: 0 10px 28px rgba(0,0,0,0.45);
    overflow: hidden;
  }
  .card--front { left: 60px; top: 60px; background: var(--card-white); }
  .card--back { left: 600px; top: 453px; background: var(--card-black); }

  .grunge-texture {
    position: absolute;
    inset: 0;
    background:
      radial-gradient(ellipse 120px 70px at 12% 22%, var(--grunge), transparent 70%),
      radial-gradient(ellipse 160px 80px at 80% 40%, var(--grunge), transparent 70%),
      radial-gradient(ellipse 140px 60px at 30% 85%, var(--grunge), transparent 70%);
    opacity: 0.7;
  }

  .brand {
    position: absolute;
    display: flex;
    align-items: center;
    gap: 12px;
  }
  .brand__mark {
    border-radius: 50%;
    border: 4px solid var(--accent);
    flex: none;
  }
  .brand__name {
    font-family: "Cinzel", "Trajan Pro", serif;
    font-weight: 600;
    color: var(--accent-soft);
    white-space: nowrap;
  }
  .card--front .brand { left: 40px; top: 120px; }
  .card--front .brand__mark { width: 46px; height: 46px; }
  .card--front .brand__name { font-size: 30px; letter-spacing: 0.5px; }

  .address {
    position: absolute;
    left: 48px;
    top: 196px;
    font-size: 15px;
    line-height: 1.45;
    color: var(--ink);
  }

  .person {
    position: absolute;
    left: 330px;
    top: 50px;
  }
  .person__name { color: var(--accent); font-size: 17px; }
  .person__role { color: var(--ink); font-size: 11px; margin-top: 2px; }

  .contact {
    position: absolute;
    left: 330px;
    top: 152px;
    list-style: none;
    font-size: 14.5px;
    color: var(--ink);
  }
  .contact li { display: flex; align-items: center; gap: 6px; line-height: 1.35; }
  .contact svg { width: 12px; height: 12px; fill: var(--accent); flex: none; }

  .card--back .brand {
    left: 0; right: 0; top: 0; bottom: 0;
    justify-content: center;
  }
  .card--back .brand__mark { width: 64px; height: 64px; }
  .card--back .brand__name { font-size: 40px; letter-spacing: 1px; }
</style>
</head>
<body>

<section class="card card--front" aria-label="Card front">
  <div class="grunge-texture" role="img" aria-label="Soft grey grunge splatter texture"></div>

  <div class="brand">
    <span class="brand__mark"></span>
    <span class="brand__name">Maple Ridge</span>
  </div>

  <p class="address">48 Harbor Mill Road,<br>Fairhaven, Oregon 97420</p>

  <div class="person">
    <p class="person__name">Employee Name</p>
    <p class="person__role">Owner</p>
  </div>

  <ul class="contact">
    <li>
      <svg viewBox="0 0 12 12" aria-hidden="true"><rect width="12" height="12" rx="2"/><path d="M3.5 2.5l1.5 1.5-1 1c.5 1.2 1.3 2 2.5 2.5l1-1 1.5 1.5-1 1C5.5 9 3 6.5 2.5 3.5z" fill="#fff"/></svg>
      541-555-0142
    </li>
    <li>
      <svg viewBox="0 0 12 12" aria-hidden="true"><rect x="3" y="1" width="6" height="3"/><rect x="1" y="4.5" width="10" height="4.5" rx="1"/><rect x="3" y="8" width="6" height="3"/></svg>
      541-555-0148
    </li>
    <li>
      <svg viewBox="0 0 12 12" aria-hidden="true"><rect y="2" width="12" height="8" rx="1"/><path d="M1 3l5 3.5L11 3" stroke="#fff" stroke-width="1" fill="none"/></svg>
      hello@mapleridge.co
    </li>
    <li>
      <svg viewBox="0 0 12 12" aria-hidden="true"><circle cx="6" cy="6" r="6"/><path d="M0 6h12M6 0c-3 3-3 9 0 12M6 0c3 3 3 9 0 12" stroke="#fff" stroke-width="0.8" fill="none"/></svg>
      www.mapleridge.co
    </li>
  </ul>
</section>

<section class="card card--back" aria-label="Card back">
  <div class="brand">
    <span class="brand__mark"></span>
    <span class="brand__name">Maple Ridge</span>
  </div>
</section>

</body>
</html>
```